I need a logo that demonstrates multiple of the same with one of a distinguishing feature. I would like something that can be recognisable in silhouette format. The business designs Management systems bespoke the to the company helping them pre-qualify for work.
Something that can demonstrate a distinction between a collective group non of which are the same in shape or size, with the largest of these not the distinguished object (or something to that effect).
This is a new business no logo or artwork exists.
Target Market(s)
Small to Medium Size enterprises in the city and rural areas. Looking to make the step up.
Industry/Entity Type
Manufacture
Contact Information for Business Card
room for, Name, Email, phone number
Font styles to use
Requirements
Must have
- would like the silhouette to be recognisable
Nice to have
- would like it to incorporate the name Clearpath Advisory Group.
- Would like the same logo to be on both business cards and on corporate shirts
Should not have
- anything that may exclude rural trade or manufacturing.
- I don't want to appear as corporate, just professional

```html
<!DOCTYPE html>
<html lang="en">
<head>
<meta charset="utf-8">
<title>Clearpath Advisory Group – Business Card</title>
<link rel="stylesheet" href="https://fonts.googleapis.com/css2?family=Open+Sans:wght@400;600;700&display=swap">
<style>
  :root {
    --backdrop: #2b2d31;
    --brand-blue: #0a4fa3;
    --card-white: #ffffff;
    --text-dark: #333333;
    --text-muted: #555555;
    --rule-grey: #b8b8b8;
    --rule-light: rgba(255, 255, 255, 0.6);
  }
  * { box-sizing: border-box; margin: 0; padding: 0; }
  html, body {
    width: 1200px;
    height: 864px;
    overflow: hidden;
    background: var(--backdrop);
    font-family: "Open Sans", Arial, sans-serif;
  }
  .stage {
    position: relative;
    width: 1200px;
    height: 864px;
  }
  .card {
    position: absolute;
    width: 580px;
    height: 330px;
    border-radius: 3px;
    box-shadow: 0 14px 30px rgba(0, 0, 0, 0.45);
  }

  /* Front: brand side */
  .card--front {
    left: 230px;
    top: 70px;
    background: var(--brand-blue);
  }
  .front-lockup {
    position: absolute;
    right: 40px;
    bottom: 48px;
    text-align: center;
    color: var(--card-white);
  }
  .front-lockup__name {
    font-weight: 700;
    font-size: 26px;
    letter-spacing: 0.2px;
    padding-bottom: 8px;
    border-bottom: 1px solid var(--rule-light);
  }

  /* Back: contact side */
  .card--back {
    left: 200px;
    top: 460px;
    background: var(--card-white);
  }
  .back-lockup {
    position: absolute;
    right: 36px;
    top: 40px;
    display: flex;
    align-items: center;
    gap: 12px;
  }
  .back-lockup__mark {
    width: 18px;
    height: 18px;
    border-radius: 50%;
    background: var(--brand-blue);
  }
  .back-lockup__name {
    font-weight: 700;
    font-size: 24px;
    color: var(--brand-blue);
    padding-bottom: 6px;
    border-bottom: 1px solid var(--rule-grey);
  }
  .holder {
    position: absolute;
    left: 40px;
    top: 128px;
    width: 510px;
    padding-bottom: 10px;
    border-bottom: 1px solid var(--rule-grey);
  }
  .holder__name {
    font-weight: 600;
    font-size: 21px;
    color: var(--brand-blue);
    line-height: 1.1;
  }
  .holder__title {
    font-size: 13px;
    color: var(--text-dark);
  }
  .contact-list {
    position: absolute;
    right: 36px;
    top: 200px;
    list-style: none;
  }
  .contact-list__item {
    display: flex;
    justify-content: flex-end;
    align-items: center;
    gap: 8px;
    font-size: 15px;
    line-height: 22px;
    color: var(--text-dark);
  }
  .contact-list__icon {
    width: 12px;
    height: 12px;
    fill: var(--brand-blue);
  }
</style>
</head>
<body>
<main class="stage">

  <section class="card card--front" aria-label="Business card front">
    <div class="front-lockup">
      <div class="front-lockup__name">Clearpath Advisory Group</div>
    </div>
  </section>

  <section class="card card--back" aria-label="Business card back">
    <div class="back-lockup">
      <span class="back-lockup__mark"></span>
      <span class="back-lockup__name">Clearpath Advisory Group</span>
    </div>

    <div class="holder">
      <div class="holder__name">Daniel Hartley</div>
      <div class="holder__title">Managing Director</div>
    </div>

    <ul class="contact-list">
      <li class="contact-list__item">044-555-0142
        <svg class="contact-list__icon" viewBox="0 0 12 12" aria-hidden="true"><path d="M2.5 1 L4.5 1 L5 3.5 L3.8 4.5 Q5 7 7.5 8.2 L8.5 7 L11 7.5 L11 9.5 Q10.5 11 9 11 Q1 10 1 3 Q1 1.5 2.5 1Z"/></svg>
      </li>
      <li class="contact-list__item">123-555-0198
        <svg class="contact-list__icon" viewBox="0 0 12 12" aria-hidden="true"><rect x="3" y="1" width="6" height="3"/><rect x="1" y="4.5" width="10" height="6.5" rx="1"/></svg>
      </li>
      <li class="contact-list__item">123-555-0176
        <svg class="contact-list__icon" viewBox="0 0 12 12" aria-hidden="true"><path d="M3.5 0.5 H8.5 A1 1 0 0 1 9.5 1.5 V10.5 A1 1 0 0 1 8.5 11.5 H3.5 A1 1 0 0 1 2.5 10.5 V1.5 A1 1 0 0 1 3.5 0.5Z M3.7 2 V9 H8.3 V2Z"/></svg>
      </li>
      <li class="contact-list__item">hello@clearpathgroup.com
        <svg class="contact-list__icon" viewBox="0 0 12 12" aria-hidden="true"><path d="M0.5 2.5 H11.5 V9.5 H0.5Z M1.5 3.2 L6 6.5 L10.5 3.2" stroke="#fff" stroke-width="0.8"/></svg>
      </li>
      <li class="contact-list__item">www.clearpathgroup.com
        <svg class="contact-list__icon" viewBox="0 0 12 12" aria-hidden="true"><path d="M5 7 L7 5 M4.5 5.5 L2.5 7.5 A1.8 1.8 0 0 0 4.5 9.5 L6.5 7.5 M7.5 6.5 L9.5 4.5 A1.8 1.8 0 0 0 7.5 2.5 L5.5 4.5" fill="none" stroke="#0a4fa3" stroke-width="1.3" stroke-linecap="round"/></svg>
      </li>
    </ul>
  </section>

</main>
</body>
</html>
```